A5 Flyer & A3 poster design for Fizz Lobes

Fizz Lobes are a fun new accesories brand based in the UK

Create an A5 Flyer , A4 poster and simple website under construction landing page.

1. A5 Flyer - Portrait

- Hand drawn example attached showing rough layout. To include 6 pictures (attached) in polaroid format hung on a line using pegs.
- Pictures to be cropped to fit in 6 same size boxes.
- Logo attached
- NEW to be written in the same pink as logo.
- Create a background in keeping with the style of the logo and images

2. A4 poster - Portrait

- The same style , colour and font as the Flyer.
- The same six images just bigger.
- Example layout attached.

COPY FOR FLYER

Brand New Quality Clip-on ears
Soft & light weight for comfortable wear
Perfect for parties, festivals & nights out
Available in a variety of quality faux fur colours with sparkle or velour centre
Great for adults or kids

Email: hello@fizzlobes.co.uk
Call: 07913 284 517
Web: www.fizzlobes.co.uk

Target Market(s)

Females 18 - 40

Industry/Entity Type

Construction

Requirements
Must have
• must be modern. no dated flyer backgrounds

```html
<!DOCTYPE html>
<html lang="en">
<head>
<meta charset="utf-8">
<title>Fizz Lobes – A4 poster and A5 flyer</title>
<link rel="stylesheet" href="https://fonts.googleapis.com/css2?family=Open+Sans:wght@400;600;700&display=swap">
<style>
  :root {
    --stage: #1e1e1e;
    --wood-light: #e6b980;
    --wood-mid: #d8a466;
    --wood-dark: #c78f50;
    --brand-pink: #e0117f;
    --ink: #2a2118;
    --paper: #ffffff;
    --string: #2b2b2b;
    --peg-red: #e8344e;
    --peg-purple: #9b35e6;
    --peg-yellow: #f7d21c;
    --peg-mint: #5ff0b4;
    --label: #ffffff;
  }
  * { box-sizing: border-box; margin: 0; padding: 0; }
  html, body { width: 1200px; height: 1000px; overflow: hidden; }
  body {
    background: var(--stage);
    font-family: "Open Sans", Arial, sans-serif;
    position: relative;
  }

  .flyer {
    position: absolute;
    width: 597px;
    height: 840px;
    overflow: hidden;
  }
  .flyer--a4 { left: 70px; top: 80px; }
  .flyer--a5 { left: 713px; top: 202px; transform: scale(0.707); transform-origin: 0 0; }

  .flyer__wood {
    position: absolute; inset: 0;
    background:
      repeating-linear-gradient(92deg, rgba(255,255,255,0.05) 0 3px, rgba(0,0,0,0) 3px 11px, rgba(120,70,20,0.05) 11px 13px, rgba(0,0,0,0) 13px 26px),
      linear-gradient(100deg, rgba(255,255,255,0.10) 0%, rgba(0,0,0,0) 30%, rgba(255,255,255,0.07) 55%, rgba(0,0,0,0.05) 100%),
      linear-gradient(180deg, var(--wood-light) 0%, var(--wood-mid) 55%, var(--wood-dark) 100%);
  }

  .brand-name {
    position: absolute; left: 28px; top: 20px;
    color: var(--brand-pink);
    font-weight: 700;
    font-size: 44px;
    line-height: 48px;
  }

  .headline {
    position: absolute; left: 362px; top: 17px; width: 220px;
    text-align: center;
    color: var(--brand-pink);
    font-weight: 700;
    font-size: 19px;
    line-height: 29px;
  }

  .product {
    position: absolute; left: 422px; width: 112px; height: 113px;
    background: var(--paper);
  }
  .product--tan { top: 80px; }
  .product--dark { top: 211px; }
  .product__shot { position: absolute; inset: 16px 8px; }
  .product--tan .product__shot {
    background: radial-gradient(ellipse 50% 50% at 50% 55%, #b98d76 0%, #c8a184 35%, #e4cdb6 65%, #ffffff 100%);
  }
  .product--dark .product__shot {
    background: radial-gradient(ellipse 50% 50% at 50% 55%, #c2163a 0%, #8a0f25 30%, #2a1216 65%, #ffffff 100%);
  }

  .features {
    position: absolute; left: 28px; top: 153px; width: 390px;
    list-style: none;
    color: var(--ink);
    font-size: 14.5px;
    line-height: 20px;
  }
  .features li {
    position: relative; padding-left: 24px; margin-bottom: 7.5px;
  }
  .features svg { position: absolute; left: 0; top: 5px; width: 11px; height: 10px; }

  .line { position: absolute; left: 0; top: 0; width: 597px; height: 840px; }

  .polaroid {
    position: absolute;
    width: 160px; height: 190px;
    background: var(--paper);
    padding: 13px 12px 34px;
    box-shadow: 0 4px 10px rgba(0,0,0,0.25);
  }
  .polaroid__photo { width: 100%; height: 100%; }
  .photo-a { background: radial-gradient(ellipse 70% 75% at 60% 55%, #f0d2b2 0%, #dbb083 28%, #8c6a4e 55%, #3a3336 80%, #1f2024 100%); }
  .photo-b { background: radial-gradient(ellipse 80% 70% at 50% 50%, #e9c3a6 0%, #c89474 35%, #7a5a48 65%, #d9d4cf 100%); }
  .photo-c { background: radial-gradient(ellipse 75% 70% at 50% 60%, #d9a987 0%, #b9805e 30%, #5b4636 60%, #26231f 100%); }
  .photo-d { background: radial-gradient(ellipse 80% 65% at 50% 60%, #e4b89d 0%, #d09e86 30%, #b99685 55%, #e8ded4 100%); }
  .photo-e { background: linear-gradient(180deg, #efe2cc 0%, #dcc3a3 22%, #c0606f 38%, #6a4232 60%, #d3a288 88%, #c69076 100%); }
  .photo-f { background: radial-gradient(ellipse 65% 70% at 50% 50%, #e6b39a 0%, #c47c63 30%, #6b3a2e 55%, #cfc2b6 85%, #ece4dc 100%); }

  .polaroid--1 { left: 20px; top: 345px; transform: rotate(6deg); }
  .polaroid--2 { left: 225px; top: 367px; transform: rotate(-2deg); }
  .polaroid--3 { left: 418px; top: 345px; transform: rotate(-4deg); }
  .polaroid--4 { left: 20px; top: 565px; transform: rotate(4deg); }
  .polaroid--5 { left: 220px; top: 578px; transform: rotate(0deg); }
  .polaroid--6 { left: 420px; top: 558px; transform: rotate(-4deg); }

  .peg {
    position: absolute; width: 11px; height: 34px; border-radius: 1px;
    left: 50%; top: -20px; margin-left: -5px;
    box-shadow: 0 1px 2px rgba(0,0,0,0.25);
  }
  .peg--red { background: var(--peg-red); }
  .peg--purple { background: var(--peg-purple); }
  .peg--yellow { background: var(--peg-yellow); }
  .peg--mint { background: var(--peg-mint); }

  .call {
    position: absolute; left: 30px; top: 784px;
    color: var(--ink);
  }
  .call__label { font-size: 13px; font-weight: 700; letter-spacing: 0.3px; }
  .call__number { font-size: 20px; font-weight: 700; margin-top: 2px; }

  .contact {
    position: absolute; left: 398px; top: 784px;
    list-style: none;
    color: var(--ink);
    font-size: 14.5px;
    line-height: 25px;
  }
  .contact li { display: flex; align-items: center; gap: 10px; }
  .contact svg { width: 14px; height: 14px; }

  .size-label {
    position: absolute; color: var(--label);
    font-size: 36px; font-weight: 400;
  }
  .size-label--a4 { left: 344px; top: 938px; }
  .size-label--a5 { left: 900px; top: 810px; }
</style>
</head>
<body>

<svg width="0" height="0" style="position:absolute">
  <defs>
    <symbol id="ear-bullet" viewBox="0 0 11 10">
      <path d="M0 0 L5.5 4 L11 0 L10 10 L5.5 7 L1 10 Z" fill="#e0117f"/>
    </symbol>
    <symbol id="icon-mail" viewBox="0 0 14 14">
      <circle cx="7" cy="7" r="7" fill="#2a2118"/>
      <rect x="3.5" y="4.5" width="7" height="5" fill="none" stroke="#e2b57c" stroke-width="1"/>
      <path d="M3.5 4.5 L7 7.3 L10.5 4.5" fill="none" stroke="#e2b57c" stroke-width="1"/>
    </symbol>
    <symbol id="icon-web" viewBox="0 0 14 14">
      <circle cx="7" cy="7" r="7" fill="#2a2118"/>
      <circle cx="7" cy="7" r="3.8" fill="none" stroke="#e2b57c" stroke-width="0.9"/>
      <path d="M3.2 7 H10.8 M7 3.2 V10.8" stroke="#e2b57c" stroke-width="0.9"/>
    </symbol>
  </defs>
</svg>

<section class="flyer flyer--a4" aria-label="A4 poster">
  <div class="flyer__wood" role="img" aria-label="Light natural wood grain background"></div>
  <div class="brand-name">Fizz<br>Lobes</div>
  <h1 class="headline">Brand New<br>Quality Clip-on ears</h1>
  <div class="product product--tan"><div class="product__shot" role="img" aria-label="Pair of tan faux fur clip-on ears with sparkle centre"></div></div>
  <div class="product product--dark"><div class="product__shot" role="img" aria-label="Pair of black faux fur clip-on ears with red velour centre"></div></div>
  <ul class="features">
    <li><svg><use href="#ear-bullet"/></svg>Brand New Quality Clip-on ears</li>
    <li><svg><use href="#ear-bullet"/></svg>Soft &amp; light weight for comfortable wear</li>
    <li><svg><use href="#ear-bullet"/></svg>Perfect for parties, festivals &amp; nights out</li>
    <li><svg><use href="#ear-bullet"/></svg>Available in a variety of quality faux fur colours<br>with sparkle or velour centre</li>
    <li><svg><use href="#ear-bullet"/></svg>Great for adults or kids</li>
  </ul>
  <svg class="line" viewBox="0 0 597 840">
    <path d="M0 345 Q300 385 597 338" fill="none" stroke="var(--string)" stroke-width="2"/>
    <path d="M0 572 Q300 588 597 548" fill="none" stroke="var(--string)" stroke-width="2"/>
  </svg>
  <div class="polaroid polaroid--1"><div class="polaroid__photo photo-a" role="img" aria-label="Photo of a woman wearing tan clip-on ears"></div><span class="peg peg--red"></span></div>
  <div class="polaroid polaroid--2"><div class="polaroid__photo photo-b" role="img" aria-label="Group photo of three friends wearing clip-on ears"></div><span class="peg peg--purple"></span></div>
  <div class="polaroid polaroid--3"><div class="polaroid__photo photo-c" role="img" aria-label="Photo of two friends at a party wearing ears"></div><span class="peg peg--yellow"></span></div>
  <div class="polaroid polaroid--4"><div class="polaroid__photo photo-d" role="img" aria-label="Photo of two friends wearing pink and black ears"></div><span class="peg peg--purple"></span></div>
  <div class="polaroid polaroid--5"><div class="polaroid__photo photo-e" role="img" aria-label="Close-up of cream and pink fur ears on a head"></div><span class="peg peg--yellow"></span></div>
  <div class="polaroid polaroid--6"><div class="polaroid__photo photo-f" role="img" aria-label="Photo of a woman wearing pink sparkle ears"></div><span class="peg peg--mint"></span></div>
  <div class="call">
    <div class="call__label">CALL NOW</div>
    <div class="call__number">07913 284 517</div>
  </div>
  <ul class="contact">
    <li><svg><use href="#icon-mail"/></svg>hello@fizzlobes.co.uk</li>
    <li><svg><use href="#icon-web"/></svg>www.fizzlobes.co.uk</li>
  </ul>
</section>

<section class="flyer flyer--a5" aria-label="A5 flyer">
  <div class="flyer__wood" role="img" aria-label="Light natural wood grain background"></div>
  <div class="brand-name">Fizz<br>Lobes</div>
  <h1 class="headline">Brand New<br>Quality Clip-on ears</h1>
  <div class="product product--tan"><div class="product__shot" role="img" aria-label="Pair of tan faux fur clip-on ears with sparkle centre"></div></div>
  <div class="product product--dark"><div class="product__shot" role="img" aria-label="Pair of black faux fur clip-on ears with red velour centre"></div></div>
  <ul class="features">
    <li><svg><use href="#ear-bullet"/></svg>Brand New Quality Clip-on ears</li>
    <li><svg><use href="#ear-bullet"/></svg>Soft &amp; light weight for comfortable wear</li>
    <li><svg><use href="#ear-bullet"/></svg>Perfect for parties, festivals &amp; nights out</li>
    <li><svg><use href="#ear-bullet"/></svg>Available in a variety of quality faux fur colours<br>with sparkle or velour centre</li>
    <li><svg><use href="#ear-bullet"/></svg>Great for adults or kids</li>
  </ul>
  <svg class="line" viewBox="0 0 597 840">
    <path d="M0 345 Q300 385 597 338" fill="none" stroke="var(--string)" stroke-width="2"/>
    <path d="M0 572 Q300 588 597 548" fill="none" stroke="var(--string)" stroke-width="2"/>
  </svg>
  <div class="polaroid polaroid--1"><div class="polaroid__photo photo-a" role="img" aria-label="Photo of a woman wearing tan clip-on ears"></div><span class="peg peg--red"></span></div>
  <div class="polaroid polaroid--2"><div class="polaroid__photo photo-b" role="img" aria-label="Group photo of three friends wearing clip-on ears"></div><span class="peg peg--purple"></span></div>
  <div class="polaroid polaroid--3"><div class="polaroid__photo photo-c" role="img" aria-label="Photo of two friends at a party wearing ears"></div><span class="peg peg--yellow"></span></div>
  <div class="polaroid polaroid--4"><div class="polaroid__photo photo-d" role="img" aria-label="Photo of two friends wearing pink and black ears"></div><span class="peg peg--purple"></span></div>
  <div class="polaroid polaroid--5"><div class="polaroid__photo photo-e" role="img" aria-label="Close-up of cream and pink fur ears on a head"></div><span class="peg peg--yellow"></span></div>
  <div class="polaroid polaroid--6"><div class="polaroid__photo photo-f" role="img" aria-label="Photo of a woman wearing pink sparkle ears"></div><span class="peg peg--mint"></span></div>
  <div class="call">
    <div class="call__label">CALL NOW</div>
    <div class="call__number">07913 284 517</div>
  </div>
  <ul class="contact">
    <li><svg><use href="#icon-mail"/></svg>hello@fizzlobes.co.uk</li>
    <li><svg><use href="#icon-web"/></svg>www.fizzlobes.co.uk</li>
  </ul>
</section>

<div class="size-label size-label--a4">A4</div>
<div class="size-label size-label--a5">A5</div>

</body>
</html>
```